Lawn Maintenance Company needs Flyer (Postcard) Design.

Hi everyone.
The majority of what I do is lawn maintenance (grass cutting and trimming/edging).

I'm pretty well open to anything (even humour) but want to stay away from the cartoon/illustration type flyer (but always receptive if you think you have something that might look good, like Pipkin (Thimbles character) :)
Simple but I guess as everyone, something that catches people's eye.

Feel free to kind of play with the name if you think it would help, I would be willing to pay extra if you thought you had a good idea for some type of logo also.

Flyer/Postcard will be front and back, front mainly outlined here, back would be a list of additional services.

Main points I want to get across.
- Professional
- Reliable
- Not like the larger companies that send students or part time
helpers
Kind of want to get those points across without necessarily saying them.

Ok, well, if you haven't rolled your eyes and headed off to the next project.................... :)

Target Market(s)

Mostly regular people with bungalow / two storey houses that don't want to do it themselves and want a nice lawn to frame their house.

Industry/Entity Type

It Company

Requirements
Must have
• Front
** Bramblecrest Landscaping and Lawn Services
** Lawn Maintenance
** (416) 555-3827
** bramblecrestyard@mailvora.com

Back
Commercial and Residential
Plaza Maintenance
Spring/Fall Clean-up
Fertilizing
Weed Prevention
Hedge Trimming
Flower Bed Design
Topdressing
Triplemix
Overseeding
Lawn & flower bed re-edging
Eavestrough Cleaning
Nice to have
• ummmm....grass. lol :)
Birds
Butterflies
Should not have
• Elaborate homes/gardens
Pictures/photos of people

**The pictures I have included are to just give you an idea of the work I do and the type of properties I do**
Please let me know if you want more pics.

```html
<!DOCTYPE html>
<html lang="en">
<head>
<meta charset="utf-8">
<title>Bramblecrest Landscaping and Lawn Services – Services Flyer</title>
<link href="https://fonts.googleapis.com/css2?family=Montserrat:wght@400;600&display=swap" rel="stylesheet">
<style>
  :root {
    --backdrop: #4a4a4a;
    --paper: #f4f5f3;
    --paper-shade: #dcdedb;
    --grass-deep: #3f8a12;
    --grass-bright: #7fcb1f;
    --ink-dark: #4d7d12;
    --ink-light: #82c41e;
    --logo-ink: #ffffff;
  }
  * { margin: 0; padding: 0; box-sizing: border-box; }
  html, body {
    width: 1023px;
    height: 1200px;
    overflow: hidden;
    background: var(--backdrop);
  }
  .flyer {
    position: absolute;
    left: 112px;
    top: 0;
    width: 798px;
    height: 1200px;
    overflow: hidden;
    background:
      repeating-linear-gradient(96deg, rgba(255,255,255,0) 0 14px, rgba(210,212,208,0.35) 14px 17px, rgba(255,255,255,0) 17px 31px),
      radial-gradient(ellipse at 50% 45%, var(--paper) 0%, var(--paper) 45%, var(--paper-shade) 100%);
    font-family: "Montserrat", sans-serif;
  }
  .grass-top {
    position: absolute;
    left: 0; top: 0;
    width: 100%;
    height: 270px;
    background: linear-gradient(to bottom, var(--grass-deep) 0%, var(--grass-bright) 30%, rgba(127,203,31,0.55) 55%, rgba(127,203,31,0) 100%);
  }
  .grass-bottom {
    position: absolute;
    left: 0; bottom: 0;
    width: 100%;
    height: 370px;
    background: linear-gradient(to top, var(--grass-deep) 0%, #4f9c16 35%, var(--grass-bright) 62%, rgba(127,203,31,0.5) 82%, rgba(127,203,31,0) 100%);
  }
  .services {
    position: absolute;
    left: 0;
    top: 312px;
    width: 100%;
    text-align: center;
    text-transform: uppercase;
    font-weight: 600;
    list-style: none;
  }
  .services-heading {
    font-size: 38px;
    font-weight: 400;
    color: var(--ink-dark);
    letter-spacing: 1px;
    margin-bottom: 30px;
  }
  .services li {
    font-size: 33px;
    line-height: 41.8px;
    letter-spacing: 0.5px;
  }
  .services li:nth-child(odd) { color: var(--ink-dark); }
  .services li:nth-child(even) { color: var(--ink-light); }
  .brand {
    position: absolute;
    left: 54px;
    bottom: 52px;
    display: flex;
    align-items: center;
    gap: 14px;
    color: var(--logo-ink);
    font-size: 17px;
    font-weight: 600;
    line-height: 1.2;
  }
  .brand-mark {
    width: 16px;
    height: 16px;
    background: var(--logo-ink);
  }
</style>
</head>
<body>
  <main class="flyer">
    <div class="grass-top" role="img" aria-label="Photo of fresh green grass blades hanging down from the top edge"></div>
    <div class="grass-bottom" role="img" aria-label="Photo of tall green grass growing up from the bottom edge"></div>

    <section>
      <h1 class="services-heading" style="position:absolute;top:268px;width:100%;text-align:center;">WE DO:</h1>
      <ul class="services" style="top:338px;">
        <li>Commercial and Residential</li>
        <li>Plaza Maintenance</li>
        <li>Spring/Fall Clean-up</li>
        <li>Fertilizing</li>
        <li>Weed Prevention</li>
        <li>Hedge Trimming</li>
        <li>Flower Bed Design</li>
        <li>Topdressing</li>
        <li>Triplemix</li>
        <li>Overseeding</li>
        <li>Lawn &amp; Flower Bed Re-edging</li>
        <li>Eavestrough Cleaning</li>
      </ul>
    </section>

    <footer class="brand">
      <span class="brand-mark"></span>
      <span class="brand-name">Bramblecrest Landscaping<br>and Lawn Services</span>
    </footer>
  </main>
</body>
</html>
```